Business Card Design for Cloud Frames

Hi we need a business card designed for a new aerial photography business we have started, we use UAV Drones to take photos for corporate, events, real estate, local government etc , the business name is Cloud Frames Australia, we have a facebook page that might help you come up with some designs - https://www.facebook.com/cloudframesaustralia

We need to have and editable AI file so that we can use different names and contact details. details for one of the cards as follow:

Dave Marsh
phone: 03 5512 4837
Mobile: 0439 175 286
email: dave@cloudframes.example.com.au
web: www.cloudframes.example.com.au

have now changed: Designer Payment:Committed

Target Market(s)

We are a Aerial Photography business using Drones and UAV

Industry/Entity Type

Business

Logo Text

Cloud Frames Australia

Requirements
Must have
• Colors to match logo and be part of Cloud Frames Brand

```html
<!DOCTYPE html>
<html lang="en">
<head>
<meta charset="utf-8">
<title>Cloud Frames Australia — Business Card</title>
<link rel="stylesheet" href="https://fonts.googleapis.com/css2?family=Titillium+Web:wght@400;600;700&display=swap">
<style>
  :root {
    --brand-blue: #1ba5e1;
    --ink: #3a3a3a;
    --logo-grey: #5b5e63;
    --paper: #ffffff;
    --canvas: #eef0f2;
    --sky-top: #4f8fd6;
    --sky-mid: #cfdcec;
    --ground: #7a8a5c;
    --ground-dark: #5d6b45;
  }
  * { margin: 0; padding: 0; box-sizing: border-box; }
  html, body {
    width: 1200px; height: 2250px; overflow: hidden;
    background: var(--canvas);
    font-family: "Titillium Web", sans-serif;
  }
  .sheet { position: relative; width: 1200px; height: 2250px; }
  .card {
    position: absolute; left: 33px; width: 1134px; height: 667px;
    background: var(--paper); overflow: hidden;
    box-shadow: 0 6px 24px rgba(0,0,0,0.12);
  }
  .card--front { top: 33px; }
  .card--back { top: 768px; }
  .card__art { position: absolute; inset: 0; width: 100%; height: 100%; }

  .brand {
    position: absolute; left: 75px; top: 52px;
    color: var(--logo-grey); font-weight: 700;
    line-height: 1; text-transform: uppercase;
  }
  .brand__name { display: block; font-size: 44px; letter-spacing: 1px; }
  .brand__region { display: block; font-size: 16px; letter-spacing: 9px; margin-top: 8px; padding-left: 3px; }

  .contact { position: absolute; left: 78px; top: 345px; }
  .contact__name {
    color: var(--brand-blue); font-weight: 700; font-size: 54px;
    line-height: 1; margin-bottom: 22px;
  }
  .contact__list { list-style: none; }
  .contact__item {
    display: flex; align-items: center; height: 57px;
    color: var(--ink); font-size: 31px; letter-spacing: 0.5px;
  }
  .contact__icon { width: 34px; height: 34px; margin-right: 36px; flex: none; fill: var(--ink); }

  .photo-area { position: absolute; inset: 0; }
</style>
</head>
<body>
<main class="sheet">

  <section class="card card--front" aria-label="Business card front">
    <svg class="card__art" viewBox="0 0 756 445" preserveAspectRatio="none">
      <defs>
        <linearGradient id="frontPhoto" x1="0" y1="0" x2="0" y2="1">
          <stop offset="0" stop-color="var(--sky-top)"/>
          <stop offset="0.25" stop-color="var(--sky-mid)"/>
          <stop offset="0.45" stop-color="#7d8076"/>
          <stop offset="1" stop-color="var(--ground)"/>
        </linearGradient>
      </defs>
      <polygon role="img" aria-label="Aerial photograph of a suburban street and houses"
               points="540,0 756,0 756,445 540,445 430,223" fill="url(#frontPhoto)"/>
      <polygon class="chevron-band" points="548,0 650,0 430,223 650,445 548,445 340,223" fill="var(--brand-blue)"/>
    </svg>

    <div class="brand">
      <span class="brand__name">Cloud Frames</span>
      <span class="brand__region">Australia</span>
    </div>

    <div class="contact">
      <h1 class="contact__name">Dave Marsh</h1>
      <ul class="contact__list">
        <li class="contact__item">
          <svg class="contact__icon" viewBox="0 0 24 24" aria-hidden="true"><path d="M6.6 10.8a15.1 15.1 0 0 0 6.6 6.6l2.2-2.2c.3-.3.7-.4 1-.2 1.1.4 2.3.6 3.6.6.6 0 1 .4 1 1V20c0 .6-.4 1-1 1A17 17 0 0 1 3 4c0-.6.4-1 1-1h3.5c.6 0 1 .4 1 1 0 1.3.2 2.5.6 3.6.1.3 0 .7-.2 1z"/></svg>
          03 5512 4837
        </li>
        <li class="contact__item">
          <svg class="contact__icon" viewBox="0 0 24 24" aria-hidden="true"><path d="M5 1h14v22H5zM7 3v5h10V3zm0 8v2h2v-2zm4 0v2h2v-2zm4 0v2h2v-2zm-8 4v2h2v-2zm4 0v2h2v-2zm4 0v2h2v-2zm-8 4v2h2v-2zm4 0v2h2v-2zm4 0v2h2v-2z"/></svg>
          0439 175 286
        </li>
        <li class="contact__item">
          <svg class="contact__icon" viewBox="0 0 24 24" aria-hidden="true"><path d="M2 5h20v14H2zm2 2v.4l8 5.3 8-5.3V7zm0 2.8V17h16V9.8l-8 5.3z"/></svg>
          dave@cloudframes.example.com.au
        </li>
        <li class="contact__item">
          <svg class="contact__icon" viewBox="0 0 24 24" aria-hidden="true"><path d="M12 2a10 10 0 1 0 0 20 10 10 0 0 0 0-20zm-1 17.9A8 8 0 0 1 4.2 10L9 14.8v1a2 2 0 0 0 2 2zm6.9-2.5a2 2 0 0 0-1.9-1.4h-1v-3a1 1 0 0 0-1-1H8v-2h2a1 1 0 0 0 1-1V7h2a2 2 0 0 0 2-2v-.4a8 8 0 0 1 2.9 12.8z"/></svg>
          www.cloudframes.example.com.au
        </li>
      </ul>
    </div>
  </section>

  <section class="card card--back" aria-label="Business card back">
    <svg class="card__art" viewBox="0 0 756 440" preserveAspectRatio="none">
      <defs>
        <linearGradient id="backPhoto" x1="0" y1="0" x2="0" y2="1">
          <stop offset="0" stop-color="var(--sky-top)"/>
          <stop offset="0.2" stop-color="var(--sky-mid)"/>
          <stop offset="0.3" stop-color="#e9eef4"/>
          <stop offset="0.36" stop-color="#8a8d84"/>
          <stop offset="0.6" stop-color="var(--ground)"/>
          <stop offset="1" stop-color="var(--ground-dark)"/>
        </linearGradient>
      </defs>
      <rect class="photo-area" role="img" aria-label="Wide aerial photograph of a suburb with a park and playground under a cloudy sky"
            width="756" height="440" fill="url(#backPhoto)"/>
      <polygon class="glass-chevron" points="600,0 650,0 420,225 650,440 600,440 368,225"
               fill="#ffffff" fill-opacity="0.35"/>
    </svg>
  </section>

</main>
</body>
</html>
```